Clinicians Prime Bold "NOT YOUR DADDY's CARD" clear Card make the card you always wanted

I need a stand out business card, I would like it to be crazy modern using a
clear plastic 30 mil card, let this be your PHD thesis in Card Design, make it fun and cutting edge. Make it Toxicology Lab meets Night Club. Colors are tans and browns with a hint of gold, because we test PEE (urine) and we call it Liquid Gold!!

Target Market(s)

it goes to Dr. Offices, but I want them to say wow Nice card, and I want our Salesmen to say" We are not your Fathers Lab" we are NEW BOLD and Different....

Industry/Entity Type

Plastic

Contact Information for Business Card

Clinician's Prime Toxicology 2876 Ridgewell Avenue NW | Atlanta, GA 30594
Phone: 404.555.0172 | Fax: 404.555.0173 my cell phone 404.555.0198 my email is Darnell@cliniciansprimetox.example

CLIA#47K9031658 | Darnell Whitfield, CEO, GED
www.cliniciansprimetox.example

Requirements
Must have
• Clear Card design, I want it to be double sided, unless you can show me a design that can only need one side because it is that GOOD
Should not have
• Should not look like a conservative lab

```html
<!DOCTYPE html>
<html lang="en">
<head>
<meta charset="utf-8">
<title>Clinician's Prime Toxicology – Clear Business Card</title>
<link rel="stylesheet" href="https://fonts.googleapis.com/css2?family=Didact+Gothic&family=Open+Sans:ital,wght@1,600&display=swap">
<style>
  :root {
    --page: #e4dfda;
    --tan-top: #b8a592;
    --tan-bottom: #8d725f;
    --brown: #6e4e3e;
    --gold: #b59a48;
    --gold-light: #e6d46a;
    --sand: #e7d8b6;
    --ink: #2c2622;
    --paper: #ffffff;
    --clear: rgba(255, 255, 255, 0.38);
    --clear-edge: rgba(255, 255, 255, 0.85);
  }
  * { box-sizing: border-box; margin: 0; padding: 0; }
  html, body { width: 1200px; height: 900px; overflow: hidden; }
  body { background: var(--page); position: relative; font-family: "Didact Gothic", Arial, sans-serif; }

  .card { position: absolute; width: 560px; height: 320px; }
  .card-shape { position: absolute; inset: 0; width: 100%; height: 100%; filter: drop-shadow(0 10px 22px rgba(60, 40, 30, 0.22)); }
  .card--back { left: 70px; top: 90px; }
  .card--front { left: 570px; top: 490px; }

  .tagline { position: absolute; font-family: "Open Sans", Arial, sans-serif; font-style: italic; font-weight: 600; font-size: 13px; white-space: nowrap; }
  .company-name { position: absolute; font-family: "Didact Gothic", Arial, sans-serif; font-weight: 400; font-size: 25px; line-height: 30px; white-space: nowrap; }
  .company-dot { position: absolute; width: 36px; height: 36px; border-radius: 50%; }

  /* back side */
  .card--back .tagline { left: 112px; top: 30px; color: var(--gold-light); }
  .card--back .company-name { left: 118px; top: 54px; color: var(--paper); }
  .card--back .company-dot { left: 64px; top: 66px; background: var(--paper); }
  .address { position: absolute; left: 110px; top: 146px; color: var(--sand); font-size: 15px; line-height: 22px; }
  .phones { position: absolute; left: 42px; top: 202px; color: var(--sand); font-size: 13px; line-height: 20px; }
  .phones span { margin-right: 12px; }
  .phones .cell { padding-left: 132px; }
  .website { position: absolute; left: 40px; top: 268px; color: var(--sand); font-size: 15px; letter-spacing: 0.2px; }

  /* front side */
  .card--front .tagline { right: 34px; top: 34px; color: var(--gold); font-size: 12px; }
  .card--front .company-name { right: 34px; top: 58px; color: var(--brown); font-size: 24px; text-align: right; }
  .card--front .company-dot { left: 262px; top: 70px; background: var(--brown); }
  .person { position: absolute; right: 34px; top: 168px; text-align: right; }
  .person__name { color: var(--brown); font-size: 22px; letter-spacing: 0.3px; }
  .person__title { color: var(--gold); font-size: 16px; margin-top: 2px; }
  .clia { position: absolute; right: 34px; top: 232px; color: var(--ink); font-size: 13px; letter-spacing: 0.5px; }
  .email { position: absolute; right: 30px; top: 278px; color: var(--ink); font-size: 14px; }
</style>
</head>
<body>

<section class="card card--back" aria-label="Card back">
  <svg class="card-shape" viewBox="0 0 560 320" aria-hidden="true">
    <defs>
      <linearGradient id="tan" x1="0" y1="0" x2="0" y2="1">
        <stop offset="0" stop-color="var(--tan-top)"/>
        <stop offset="1" stop-color="var(--tan-bottom)"/>
      </linearGradient>
      <clipPath id="back-round"><rect width="560" height="320" rx="16"/></clipPath>
    </defs>
    <g clip-path="url(#back-round)">
      <rect width="560" height="320" fill="var(--clear)"/>
      <path d="M0 0 H400 C350 80 320 190 345 320 H0 Z" fill="url(#tan)"/>
      <path d="M400 0 C350 80 320 190 345 320" fill="none" stroke="var(--gold)" stroke-width="7"/>
      <path d="M418 0 C372 80 346 190 366 320" fill="none" stroke="var(--gold)" stroke-width="1.5" opacity="0.7"/>
    </g>
    <rect x="0.75" y="0.75" width="558.5" height="318.5" rx="16" fill="none" stroke="var(--clear-edge)" stroke-width="1.5"/>
  </svg>

  <p class="tagline">Fast Answers, Clear Reports, Real Support</p>
  <span class="company-dot" aria-hidden="true"></span>
  <h1 class="company-name">Clinician's Prime<br>Toxicology</h1>
  <p class="address">2876 Ridgewell Avenue NW<br>Suite B, Atlanta, GA 30594</p>
  <p class="phones">
    <span>O : 404 - 555 - 0172</span><span>F : 404 - 555 - 0173</span><br>
    <span class="cell">C : 404 - 555 - 0198</span>
  </p>
  <p class="website">www.cliniciansprimetox.example</p>
</section>

<section class="card card--front" aria-label="Card front">
  <svg class="card-shape" viewBox="0 0 560 320" aria-hidden="true">
    <defs>
      <clipPath id="front-round"><rect width="560" height="320" rx="16"/></clipPath>
    </defs>
    <g clip-path="url(#front-round)">
      <rect width="560" height="320" fill="var(--clear)"/>
      <path d="M130 0 H560 V320 H245 C262 200 220 80 130 0 Z" fill="var(--paper)"/>
      <path d="M130 0 C220 80 262 200 245 320" fill="none" stroke="var(--gold)" stroke-width="7"/>
      <path d="M112 0 C200 80 240 200 224 320" fill="none" stroke="var(--brown)" stroke-width="1.5" opacity="0.6"/>
    </g>
    <rect x="0.75" y="0.75" width="558.5" height="318.5" rx="16" fill="none" stroke="var(--clear-edge)" stroke-width="1.5"/>
  </svg>

  <p class="tagline">Fast Answers, Clear Reports, Real Support</p>
  <span class="company-dot" aria-hidden="true"></span>
  <h2 class="company-name">Clinician's Prime<br>Toxicology</h2>
  <div class="person">
    <p class="person__name">Darnell Whitfield</p>
    <p class="person__title">CEO, GED</p>
  </div>
  <p class="clia">CLIA : 47K9031658</p>
  <p class="email">Darnell@cliniciansprimetox.example</p>
</section>

</body>
</html>
```